practice letterhead

I need a letterhead design for a new company that is a veterinary specialty company. I am conservative. I want it to look professional - not "cutesy"

I need my name, credentials, address, phone number and website/email on it.

My personal information is as follows: Marisol Tedder, DVM, DACVIM (Neurology) Certified Veterinary Pain Practitioner (or CVPP) Certified Canine Rehabilitation Therapist (or CCRT) 4170 Larkfield Hwy Brenton, MA 02194 508-347-6620 marisol.tedder@petspineandcare.com www.petspineandcare.com

```html
<!DOCTYPE html>
<html lang="en">
<head>
<meta charset="utf-8">
<title>Practice Letterhead and Envelope</title>
<link href="https://fonts.googleapis.com/css2?family=Arimo:wght@400;600;700&display=swap" rel="stylesheet">
<style>
  :root {
    --backdrop: #525252;
    --paper: #ffffff;
    --sage: #6a9488;
    --navy: #17323f;
    --ink: #1f3340;
    --faint: #eff1f1;
    --rule: #8a9aa2;
  }
  * { margin: 0; padding: 0; box-sizing: border-box; }
  html, body { width: 1200px; height: 1000px; overflow: hidden; }
  body {
    background: var(--backdrop);
    font-family: "Arimo", Arial, sans-serif;
    position: relative;
  }
  .letterhead {
    position: absolute; left: 18px; top: 85px;
    width: 539px; height: 799px;
    background: var(--paper);
    overflow: hidden;
  }
  .envelope {
    position: absolute; left: 455px; top: 250px;
    width: 690px; height: 300px;
    background: var(--paper);
    overflow: hidden;
  }
  .edge-art { position: absolute; left: 0; top: 0; }
  .edge-art .band { fill: var(--sage); }
  .edge-art .swoosh { fill: var(--navy); }
  .faint-mark {
    position: absolute; border-radius: 50%;
    background: var(--faint);
  }
  .letterhead .faint-mark { left: 165px; top: 320px; width: 250px; height: 250px; }
  .envelope .faint-mark { left: 460px; top: 75px; width: 180px; height: 180px; }

  .brand { position: absolute; display: flex; align-items: center; gap: 9px; }
  .brand-dot {
    width: 40px; height: 40px; border-radius: 50%;
    border: 3px solid var(--sage); flex: none;
  }
  .brand-name {
    color: var(--sage); font-weight: 600;
    line-height: 1.2; font-size: 13.5px;
    white-space: nowrap;
  }
  .letterhead .brand { left: 288px; top: 34px; }
  .envelope .brand { left: 72px; top: 38px; }

  .return-address {
    position: absolute; left: 150px; top: 100px;
    font-size: 9.5px; color: var(--ink); font-weight: 600;
    white-space: nowrap;
  }

  .sender {
    position: absolute; left: 115px; top: 739px;
    width: 100px; text-align: right; color: var(--ink);
  }
  .sender-name { font-size: 10px; font-weight: 700; white-space: nowrap; }
  .sender-creds { font-size: 6.5px; line-height: 1.45; margin-top: 4px; white-space: nowrap; }
  .divider {
    position: absolute; left: 224px; top: 737px;
    width: 1px; height: 42px; background: var(--rule);
  }
  .contact-list {
    position: absolute; left: 234px; top: 739px;
    list-style: none; font-size: 6.5px; color: var(--ink);
  }
  .contact-list li { display: flex; align-items: center; gap: 4px; height: 10.5px; white-space: nowrap; }
  .contact-icon { width: 7px; height: 7px; flex: none; }
</style>
</head>
<body>

<section class="letterhead" aria-label="Letterhead">
  <svg class="edge-art" width="539" height="799" viewBox="0 0 539 799">
    <path class="band" d="M0,0 L65,0 C22,250 22,560 62,799 L0,799 Z"/>
    <path class="swoosh" d="M36,345 C44,560 78,700 127,799 L75,799 C52,700 38,560 36,345 Z"/>
  </svg>
  <div class="faint-mark" role="img" aria-label="Faint practice emblem"></div>

  <div class="brand">
    <span class="brand-dot"></span>
    <span class="brand-name">Pet Spine and Comfort Care<br>Center of the Northeast</span>
  </div>

  <div class="sender">
    <div class="sender-name">Marisol Tedder</div>
    <div class="sender-creds">DVM, DACVIM (Neurology)<br>CVPP, CCRT</div>
  </div>
  <div class="divider"></div>
  <ul class="contact-list">
    <li><svg class="contact-icon" viewBox="0 0 8 8"><rect width="8" height="8" rx="1.5" fill="#17323f"/><path d="M2.3,2 L3.3,2 L3.6,3.2 L3,3.6 C3.3,4.3 3.7,4.7 4.4,5 L4.8,4.4 L6,4.7 L6,5.7 C4,5.7 2.3,4 2.3,2 Z" fill="#fff"/></svg>508-347-6620</li>
    <li><svg class="contact-icon" viewBox="0 0 8 8"><rect width="8" height="8" rx="1.5" fill="#17323f"/><rect x="1.8" y="2.5" width="4.4" height="3" fill="none" stroke="#fff" stroke-width=".7"/><path d="M1.8,2.5 L4,4.2 L6.2,2.5" fill="none" stroke="#fff" stroke-width=".7"/></svg>marisol.tedder@petspineandcare.com</li>
    <li><svg class="contact-icon" viewBox="0 0 8 8"><rect width="8" height="8" rx="1.5" fill="#17323f"/><circle cx="4" cy="4" r="2.2" fill="none" stroke="#fff" stroke-width=".7"/><path d="M1.8,4 H6.2 M4,1.8 V6.2" stroke="#fff" stroke-width=".5"/></svg>www.petspineandcare.com</li>
    <li><svg class="contact-icon" viewBox="0 0 8 8"><rect width="8" height="8" rx="1.5" fill="#17323f"/><path d="M4,6.5 C3,5.2 2.4,4.3 2.4,3.4 A1.6,1.6 0 0 1 5.6,3.4 C5.6,4.3 5,5.2 4,6.5 Z" fill="#fff"/></svg>4170 Larkfield Hwy Brenton, MA 02194</li>
  </ul>
</section>

<section class="envelope" aria-label="Envelope">
  <svg class="edge-art" width="690" height="300" viewBox="0 0 690 300">
    <path class="band" d="M0,0 L70,0 C52,120 85,245 185,300 L0,300 Z"/>
    <path class="swoosh" d="M58,135 C66,220 110,272 185,300 L125,300 C86,268 64,215 58,135 Z"/>
  </svg>
  <div class="faint-mark" role="img" aria-label="Faint practice emblem"></div>

  <div class="brand">
    <span class="brand-dot"></span>
    <span class="brand-name">Pet Spine and Comfort Care<br>Center of the Northeast</span>
  </div>
  <div class="return-address">4170 Larkfield Hwy Brenton, MA 02194</div>
</section>

</body>
</html>
```